Real Estate Sales Brokerage

Design a modern and fresh looking standard size business card, incorporate our logo's color scheme and modern appearance with head shot photo on front side and incorporate our log on the back side

Target Market(s)

Residential Home sales

Industry/Entity Type

Real Estate Agent

Font styles to use
Sans Serif

Colors

Designer to choose colors to be used in the design.

Requirements
Must have
• fresh, modern, not too busy, incorporate head shot in front of the card, incorporate logo in front and back of the card. Use logo design scheme as appropriate.
Nice to have
• horizontal and vertical options to compare would be nice.

```html
<!DOCTYPE html>
<html lang="en">
<head>
<meta charset="utf-8">
<title>Harborline Home Realty – Business Card</title>
<link rel="stylesheet" href="https://fonts.googleapis.com/css2?family=Roboto:wght@400;500;700&display=swap">
<style>
  :root {
    --stage: #c9c9c9;
    --olive: #625e36;
    --olive-dark: #56522c;
    --gold: #f2d24a;
    --gold-soft: #d9bd3f;
    --white: #ffffff;
    --photo-a: #2c3e6b;
    --photo-b: #dcdcd8;
  }
  * { margin: 0; padding: 0; box-sizing: border-box; }
  html, body { width: 900px; height: 1200px; overflow: hidden; }
  body {
    background: radial-gradient(ellipse at 50% 45%, #dedede 0%, var(--stage) 75%);
    font-family: "Roboto", Arial, sans-serif;
    position: relative;
  }
  .card {
    position: absolute;
    left: 82px;
    width: 740px;
    height: 433px;
    overflow: hidden;
    box-shadow: 0 4px 10px rgba(0,0,0,0.25);
  }
  .card-front { top: 132px; border-radius: 0 45px 0 45px; background: var(--white); }
  .card-back {
    top: 632px;
    border-radius: 45px 0 45px 0;
    background: radial-gradient(ellipse 380px 180px at 50% 0%, #d8bb48 0%, #8f8640 45%, var(--olive) 100%);
  }
  .front-waves { position: absolute; inset: 0; }
  .headshot {
    position: absolute;
    left: 440px; top: 8px;
    width: 300px; height: 425px;
    background: linear-gradient(180deg, var(--photo-b) 0%, #9aa3b8 35%, var(--photo-a) 70%, #1f2d52 100%);
    border-radius: 120px 120px 0 0;
  }
  .brand {
    position: absolute;
    display: flex;
    align-items: center;
    gap: 16px;
  }
  .brand-mark { width: 22px; height: 22px; }
  .brand-name {
    font-weight: 500;
    font-size: 27px;
    line-height: 30px;
    letter-spacing: 0.5px;
    text-transform: uppercase;
  }
  .card-front .brand { left: 44px; top: 58px; }
  .card-front .brand-mark { background: var(--gold); }
  .card-front .brand-name { color: var(--olive); }
  .agent { position: absolute; left: 66px; top: 272px; color: var(--white); }
  .agent-name { font-weight: 700; font-size: 23px; letter-spacing: 0.3px; }
  .agent-title { color: var(--gold); font-weight: 500; font-size: 15px; margin-top: 3px; letter-spacing: 0.3px; }
  .contacts { list-style: none; margin-top: 14px; }
  .contacts li { display: flex; align-items: center; gap: 10px; font-size: 16px; height: 24px; }
  .contacts svg { width: 16px; height: 16px; flex: none; }
  .card-back .brand { left: 50%; top: 158px; transform: translateX(-50%); }
  .card-back .brand-mark { background: var(--gold); }
  .card-back .brand-name { color: var(--white); }
  .address {
    position: absolute; left: 0; right: 0; top: 374px;
    text-align: center; color: var(--white); font-size: 15px; letter-spacing: 0.2px;
  }
</style>
</head>
<body>

<section class="card card-front">
  <svg class="front-waves" viewBox="0 0 740 433" width="740" height="433" aria-hidden="true">
    <defs>
      <linearGradient id="oliveFill" x1="0" y1="0" x2="0" y2="1">
        <stop offset="0" stop-color="#a69a48"/>
        <stop offset="0.35" stop-color="#6b6638"/>
        <stop offset="1" stop-color="#625e36"/>
      </linearGradient>
    </defs>
    <path d="M0,178 C120,172 260,200 460,248 L460,262 C260,222 120,196 0,196 Z" fill="#f2d24a"/>
    <path d="M0,212 C150,205 300,232 460,262 L460,272 C300,246 150,222 0,226 Z" fill="#f2d24a"/>
    <path d="M0,196 C140,198 300,226 460,256 L460,262 C300,236 140,206 0,212 Z" fill="#6b6638"/>
    <path d="M0,262 C160,248 320,258 460,272 L740,200 L740,433 L0,433 Z" fill="url(#oliveFill)"/>
    <path d="M600,190 L740,150 L740,205 L640,220 Z" fill="#625e36"/>
  </svg>

  <div class="headshot" role="img" aria-label="Head-and-shoulders portrait of the agent in a navy suit and red tie"></div>

  <div class="brand">
    <span class="brand-mark"></span>
    <span class="brand-name">Harborline<br>Home<br>Realty</span>
  </div>

  <div class="agent">
    <h1 class="agent-name">DANIEL MERCER</h1>
    <p class="agent-title">MANAGING DIRECTOR</p>
    <ul class="contacts">
      <li>
        <svg viewBox="0 0 16 16"><rect width="16" height="16" rx="3" fill="#f2d24a"/><rect x="5" y="3" width="6" height="10" rx="1" fill="none" stroke="#625e36" stroke-width="1.3"/></svg>
        555.014.2368
      </li>
      <li>
        <svg viewBox="0 0 16 16"><rect width="16" height="16" rx="3" fill="#f2d24a"/><rect x="3" y="4.5" width="10" height="7" fill="none" stroke="#625e36" stroke-width="1.2"/><path d="M3,4.5 L8,9 L13,4.5" fill="none" stroke="#625e36" stroke-width="1.2"/></svg>
        dan@harborlinehomerealty.com
      </li>
      <li>
        <svg viewBox="0 0 16 16"><rect width="16" height="16" rx="3" fill="#f2d24a"/><circle cx="8" cy="8" r="4.5" fill="none" stroke="#625e36" stroke-width="1.2"/><path d="M3.5,8 H12.5 M8,3.5 C6,6 6,10 8,12.5 C10,10 10,6 8,3.5" fill="none" stroke="#625e36" stroke-width="1"/></svg>
        www.harborlinehomerealty.com
      </li>
    </ul>
  </div>
</section>

<section class="card card-back">
  <div class="brand">
    <span class="brand-mark"></span>
    <span class="brand-name">Harborline<br>Home<br>Realty</span>
  </div>
  <p class="address">418 W. Bayview Ave, Suite 1207, P.O. Box 40215</p>
</section>

</body>
</html>
```